Copper Ridge Business Cards For New Startup

I am looking for you to design some business cards for a new startup https://copperridgehub.example. I have supplied logo, brand guidelines and our signatures as a guide.

We need this to reflect the brand guidelines and the website for brand consistency,

What is Copper Ridge?

Mallorca's Business Growth Community
Join your new business community full of passionate entrepreneurs who
love to solve problems and help each other grow together!

Any questions you can ask.

Target Market(s)

Business to Business

Contact Information for Business Card

These are attached (signatures) to the job

Font styles to use
Other font styles liked:
• Open Sans

Requirements
Must have
• Match design guidelines
Nice to have
• Photos of our faces so people remember us

```html
<!DOCTYPE html>
<html lang="en">
<head>
<meta charset="utf-8">
<title>Copper Ridge Business Cards</title>
<link href="https://fonts.googleapis.com/css2?family=Open+Sans:wght@400;600;700&display=swap" rel="stylesheet">
<style>
  :root {
    --olive: #7b8a27;
    --olive-light: #8d9b34;
    --olive-dark: #66751c;
    --olive-text: #6e7d1e;
    --line: #5d6b17;
    --paper: #ffffff;
    --ink: #2d2d2d;
    --backdrop: #e9e7e1;
    --photo-a: #e8c98a;
    --photo-b: #b9a48e;
  }
  * { box-sizing: border-box; margin: 0; padding: 0; }
  html, body { width: 1200px; height: 900px; overflow: hidden; }
  body {
    background: var(--backdrop);
    font-family: "Open Sans", Arial, sans-serif;
    display: flex;
    flex-direction: column;
    align-items: center;
    justify-content: center;
    gap: 40px;
  }
  .card {
    position: relative;
    width: 640px;
    height: 366px;
    border-radius: 4px;
    overflow: hidden;
    box-shadow: 0 6px 18px rgba(0,0,0,0.18);
  }

  /* Back side */
  .card-back {
    background: linear-gradient(160deg, var(--olive-dark), var(--olive) 55%, var(--olive-light));
    display: flex;
    align-items: center;
    justify-content: center;
  }
  .brand {
    display: flex;
    align-items: center;
    gap: 16px;
    color: var(--paper);
  }
  .brand-mark {
    width: 70px;
    height: 70px;
    border: 3px solid var(--paper);
    border-radius: 50%;
  }
  .brand-name {
    font-weight: 600;
    font-size: 34px;
    letter-spacing: 1px;
    text-transform: uppercase;
  }

  /* Front side */
  .card-front { background: var(--paper); }
  .front-panel {
    position: absolute;
    left: 0; top: 0;
    width: 372px; height: 100%;
    background: linear-gradient(150deg, var(--olive-light), var(--olive) 50%, var(--olive-dark));
    display: flex;
    flex-direction: column;
    align-items: center;
    padding-top: 78px;
    color: var(--paper);
  }
  .front-panel .brand-mark { width: 116px; height: 116px; border-width: 3px; }
  .front-panel .brand-name { font-size: 27px; margin-top: 16px; }

  .divider {
    position: absolute;
    left: 0; right: 0;
    top: 300px;
    height: 2px;
    background: var(--line);
  }

  .details {
    position: absolute;
    left: 392px; top: 0;
    width: 232px; height: 100%;
  }
  .portrait {
    position: absolute;
    right: 0; top: 22px;
    width: 100px; height: 100px;
    border-radius: 18px;
    background: linear-gradient(135deg, var(--photo-a), var(--photo-b));
  }
  .person-name {
    position: absolute;
    top: 138px; left: 0;
    font-size: 20px;
    font-weight: 700;
    color: var(--olive-text);
    white-space: nowrap;
  }
  .person-role {
    position: absolute;
    top: 166px; left: 0;
    font-size: 10.5px;
    color: var(--ink);
    white-space: nowrap;
  }
  .contact-list {
    position: absolute;
    top: 192px; left: 0;
    list-style: none;
  }
  .contact-item {
    display: flex;
    align-items: center;
    gap: 8px;
    font-size: 12.5px;
    color: var(--ink);
    height: 25px;
    white-space: nowrap;
  }
  .contact-item svg { width: 16px; height: 16px; flex: none; }
  .contact-web { color: var(--olive-text); font-weight: 700; }
  .social-row {
    position: absolute;
    top: 316px; left: 0;
    display: flex;
    gap: 8px;
    list-style: none;
  }
  .social-dot {
    width: 26px; height: 26px;
    border-radius: 50%;
    background: var(--olive-text);
  }
</style>
</head>
<body>

  <section class="card card-back" aria-label="Business card back">
    <div class="brand">
      <span class="brand-mark"></span>
      <span class="brand-name">Copper Ridge</span>
    </div>
  </section>

  <section class="card card-front" aria-label="Business card front">
    <div class="front-panel">
      <span class="brand-mark"></span>
      <span class="brand-name">Copper Ridge</span>
    </div>
    <div class="divider"></div>
    <div class="details">
      <div class="portrait" role="img" aria-label="Portrait photo of Hannah Calloway"></div>
      <h1 class="person-name">Hannah Calloway</h1>
      <p class="person-role">Relationship Director | Copper Ridge</p>
      <ul class="contact-list">
        <li class="contact-item">
          <svg viewBox="0 0 16 16" fill="none" stroke="#6e7d1e" stroke-width="1.4"><rect x="4" y="1.5" width="8" height="13" rx="1.5"/><line x1="7" y1="12" x2="9" y2="12"/></svg>
          +44 7700 900 482
        </li>
        <li class="contact-item">
          <svg viewBox="0 0 16 16"><rect x="1" y="3" width="14" height="10" rx="1" fill="#6e7d1e"/><path d="M1.5 3.5 L8 9 L14.5 3.5" fill="none" stroke="#fff" stroke-width="1.2"/></svg>
          hc@copperridgehub.example
        </li>
        <li class="contact-item contact-web">
          <svg viewBox="0 0 16 16" fill="none" stroke="#6e7d1e" stroke-width="1.3"><circle cx="8" cy="8" r="6.5"/><ellipse cx="8" cy="8" rx="3" ry="6.5"/><line x1="1.5" y1="8" x2="14.5" y2="8"/></svg>
          copperridgehub.example
        </li>
      </ul>
      <ul class="social-row" aria-label="Social profiles">
        <li class="social-dot"></li>
        <li class="social-dot"></li>
        <li class="social-dot"></li>
        <li class="social-dot"></li>
        <li class="social-dot"></li>
      </ul>
    </div>
  </section>

</body>
</html>
```